Modern Label for cleaning products for the brand Voralux

We need a label design for our line of cleaning products. The label should feature our logo and an image to identify the product's intended use. I've added our logo and an image for use. This only concerns the design of the label on the front of the bottle.

Label dimensions:
Label 1 (500ml bottle with spray): width 58mm x height 115mm
Label 2: (1L bottle): width 73mm x height 140mm
The design must be consistent for both bottles which you find in the pictures.

The bottles to be labeled are white. See the attachment for a photo of the bottles.

The photo must also appear on the label to identify the product's intended use.

Product information:
Brand: Voralux
Product: Sanitary Cleaner

This text must be placed on the label:
"Cleans, descales & freshens. followed with this text: "Ideal for quick and powerful cleaning. A ready-to-use product for everyday use."

- Mention the seperate USP's: Sanitary, Bathroom, Toilet, Wet areas

Appearance: This is a consumer product, but it must have a professional appearance. We would like to see a design that use the color blue from our logo.

Target Market(s)

Consumers who take care of their homes and want to maintain it the correct (professional) way

Font styles to use
Sans Serif

Colors
0054AA
0677BA
7BADD7
CADEEF
E8F1F8

Requirements
Must have
• USP's + use of image and logo + blend in 1 design
Nice to have
• Keep the color of the logo in the design
Should not have
• Comic sans

```html
<!DOCTYPE html>
<html lang="en">
<head>
<meta charset="utf-8">
<title>Voralux Sanitary Cleaner – Labels</title>
<link href="https://fonts.googleapis.com/css2?family=Exo+2:ital,wght@0,400;0,500;0,600;0,700;0,800;1,700&display=swap" rel="stylesheet">
<style>
  :root {
    --blue-deep: #0054AA;
    --blue: #0677BA;
    --blue-bright: #0a8ad3;
    --blue-panel: #0c4c98;
    --blue-light: #7BADD7;
    --blue-pale: #CADEEF;
    --blue-mist: #E8F1F8;
    --yellow: #f2e600;
    --ink: #111111;
    --white: #ffffff;
  }
  * { box-sizing: border-box; margin: 0; padding: 0; }
  html, body { width: 1200px; height: 898px; overflow: hidden; background: var(--white); }
  body { position: relative; font-family: "Exo 2", sans-serif; }

  .label {
    position: absolute;
    width: 394px; height: 775px;
    border-radius: 22px;
    overflow: hidden;
    background: var(--white);
    transform-origin: top left;
  }
  .label--500 { left: 203px; top: 205px; transform: scale(0.82); }
  .label--1l  { left: 598px; top: 66px; }

  .photo-floor {
    position: absolute; left: 0; top: 0; width: 394px; height: 270px;
    background:
      linear-gradient(180deg, rgba(244,238,230,.95) 0%, rgba(232,214,192,.6) 7%, rgba(232,214,192,0) 16%),
      radial-gradient(ellipse 70% 45% at 55% 30%, rgba(226,178,126,.55) 0%, rgba(226,178,126,0) 100%),
      linear-gradient(165deg, #d0a070 0%, #c08650 30%, #a86c38 62%, #8d5628 100%);
  }
  .photo-bath {
    position: absolute; left: 0; top: 395px; width: 394px; height: 320px;
    background:
      linear-gradient(180deg, rgba(255,255,255,0) 0%, rgba(255,255,255,0) 62%, rgba(170,170,172,.75) 82%, rgba(150,150,152,.9) 100%),
      linear-gradient(90deg, #86878a 0%, #a3a4a6 12%, #8f9092 22%, #c6c6c8 34%, #ececed 46%, #f7f7f8 62%, #f1f1f2 80%, #d3d3d5 90%, #a2a3a5 100%);
  }

  .bands { position: absolute; left: 0; top: 0; width: 394px; height: 775px; }

  .tag {
    position: absolute; left: 0; top: 0; width: 131px; height: 61px;
    background: var(--blue);
    border-bottom-right-radius: 20px;
    padding: 10px 0 0 16px;
    color: var(--white);
    font-size: 13px; font-weight: 600; line-height: 12.5px;
    text-transform: uppercase;
  }
  .tag .hl { color: var(--yellow); font-weight: 500; }

  .brand {
    position: absolute; left: 0; right: 0; top: 54px;
    text-align: center;
  }
  .brand-dot {
    display: block; margin: 0 auto;
    width: 116px; height: 116px; border-radius: 50%;
    background: var(--blue);
    border: 8px solid var(--white);
  }
  .brand-name {
    display: block; margin-top: 10px;
    font-size: 52px; font-weight: 800; line-height: 52px;
    color: var(--ink); letter-spacing: 1.5px;
  }

  .title {
    position: absolute; left: 0; right: 0; top: 258px;
    text-align: center; color: var(--white);
  }
  .title-sub { display: block; font-size: 42px; font-weight: 500; line-height: 44px; padding-left: 6px; }
  .title-main { display: block; font-size: 86px; font-weight: 800; line-height: 58px; letter-spacing: -1px; margin-left: -6px; }
  .rule {
    position: absolute; left: 26px; right: 40px; top: 361px;
    height: 1px; background: var(--blue-light);
  }
  .claim {
    position: absolute; left: 0; right: 6px; top: 367px;
    text-align: center; color: var(--white);
    font-size: 15.5px; font-weight: 700; letter-spacing: 0.2px;
  }

  .suitable {
    position: absolute; left: 18px; top: 389px; width: 358px; height: 74px;
    background: var(--blue-panel);
    border-radius: 0 0 10px 10px;
    overflow: hidden;
  }
  .suitable-title {
    position: absolute; left: 52px; top: 5px;
    color: var(--yellow); font-size: 10px; font-weight: 700; font-style: italic;
  }
  .uses { position: absolute; left: 0; top: 0; width: 189px; height: 74px; }
  .use {
    position: absolute; display: flex; align-items: center; gap: 6px;
    color: var(--white); font-size: 12.5px; font-weight: 700;
  }
  .use svg { width: 11px; height: 11px; fill: var(--blue-light); }
  .use--toilet { left: 20px; top: 23px; }
  .use--wet { left: 98px; top: 21px; }
  .use--sanitary { left: 13px; top: 46px; }
  .use--bath { left: 98px; top: 46px; }
  .uses .divider-v { position: absolute; left: 86px; top: 20px; width: 1px; height: 48px; background: rgba(123,173,215,.35); }
  .uses .divider-h { position: absolute; left: 8px; top: 42px; width: 175px; height: 1px; background: rgba(123,173,215,.35); }
  .photo-tiles {
    position: absolute; left: 189px; top: 5px; width: 164px; height: 69px;
    background: linear-gradient(160deg, #ececec 0%, #d6d6d6 45%, #a9a9a9 75%, #7d7d7d 100%);
  }

  .footer-left {
    position: absolute; left: 12px; top: 722px;
    font-size: 14.5px; font-weight: 500; line-height: 13.5px;
    color: var(--white); text-transform: uppercase;
  }
  .footer-left .hl { color: var(--yellow); }
  .net {
    position: absolute; right: 21px; top: 720px; text-align: right; color: var(--white);
  }
  .net-label { display: block; font-size: 12px; font-weight: 500; line-height: 14px; }
  .net-value { display: block; font-size: 36px; font-weight: 500; line-height: 36px; }
</style>
</head>
<body>

  <section class="label label--500" aria-label="Sanitary Cleaner label, 500 ml">
    <div class="photo-floor" role="img" aria-label="Photo of a polished wooden parquet floor"></div>
    <div class="photo-bath" role="img" aria-label="Photo of a clean modern bathroom with shower, basin and tiled bath"></div>
    <svg class="bands" viewBox="0 0 394 775" aria-hidden="true">
      <defs>
        <linearGradient id="band500" x1="0" x2="1" y1="0" y2="0">
          <stop offset="0" stop-color="#0054AA"/>
          <stop offset=".5" stop-color="#0a8ad3"/>
          <stop offset="1" stop-color="#0054AA"/>
        </linearGradient>
      </defs>
      <path d="M0 262 Q197 250 394 262 L394 415 L0 415 Z" fill="url(#band500)"/>
      <path d="M0 262 Q197 250 394 262" fill="none" stroke="#7BADD7" stroke-width="2"/>
      <path d="M0 710 Q197 696 394 710 L394 775 L0 775 Z" fill="url(#band500)"/>
      <path d="M0 710 Q197 696 394 710" fill="none" stroke="#7BADD7" stroke-width="2"/>
    </svg>
    <div class="tag"><span class="hl">A ready-to-use</span><br>product for<br>everyday use</div>
    <div class="brand"><span class="brand-dot"></span><span class="brand-name">voralux</span></div>
    <h1 class="title"><span class="title-sub">Sanitary</span><span class="title-main">Cleaner</span></h1>
    <div class="rule"></div>
    <p class="claim">CLEANS, DESCALES &amp; FRESHENS</p>
    <div class="suitable">
      <span class="suitable-title">SUITABLE FOR</span>
      <div class="uses">
        <span class="divider-v"></span><span class="divider-h"></span>
        <span class="use use--toilet"><svg viewBox="0 0 12 12"><path d="M2 1h2v5h6l-1 3H6v2H3V8L2 6z"/></svg>Toilet</span>
        <span class="use use--wet"><svg viewBox="0 0 12 12"><path d="M1 11V6a5 5 0 0 1 10 0h-2a3 3 0 0 0-6 0v5z"/></svg>Wet Areas</span>
        <span class="use use--sanitary"><svg viewBox="0 0 12 12"><path d="M4 0h2v5l4 7H1l3-7z"/></svg>Sanitary</span>
        <span class="use use--bath"><svg viewBox="0 0 12 12"><path d="M1 2h8v2H3v2h6v2H3v3H1z"/></svg>Bathroom</span>
      </div>
      <div class="photo-tiles" role="img" aria-label="Photo of stacked grey floor tiles"></div>
    </div>
    <p class="footer-left">Ideal for<br><span class="hl">quick and powerful<br>cleaning.</span></p>
    <p class="net"><span class="net-label">NET WT.</span><span class="net-value">500ml</span></p>
  </section>

  <section class="label label--1l" aria-label="Sanitary Cleaner label, 1 litre">
    <div class="photo-floor" role="img" aria-label="Photo of a polished wooden parquet floor"></div>
    <div class="photo-bath" role="img" aria-label="Photo of a clean modern bathroom with shower, basin and tiled bath"></div>
    <svg class="bands" viewBox="0 0 394 775" aria-hidden="true">
      <defs>
        <linearGradient id="band1l" x1="0" x2="1" y1="0" y2="0">
          <stop offset="0" stop-color="#0054AA"/>
          <stop offset=".5" stop-color="#0a8ad3"/>
          <stop offset="1" stop-color="#0054AA"/>
        </linearGradient>
      </defs>
      <path d="M0 262 Q197 250 394 262 L394 415 L0 415 Z" fill="url(#band1l)"/>
      <path d="M0 262 Q197 250 394 262" fill="none" stroke="#7BADD7" stroke-width="2"/>
      <path d="M0 710 Q197 696 394 710 L394 775 L0 775 Z" fill="url(#band1l)"/>
      <path d="M0 710 Q197 696 394 710" fill="none" stroke="#7BADD7" stroke-width="2"/>
    </svg>
    <div class="tag"><span class="hl">A ready-to-use</span><br>product for<br>everyday use</div>
    <div class="brand"><span class="brand-dot"></span><span class="brand-name">voralux</span></div>
    <h1 class="title"><span class="title-sub">Sanitary</span><span class="title-main">Cleaner</span></h1>
    <div class="rule"></div>
    <p class="claim">CLEANS, DESCALES &amp; FRESHENS</p>
    <div class="suitable">
      <span class="suitable-title">SUITABLE FOR</span>
      <div class="uses">
        <span class="divider-v"></span><span class="divider-h"></span>
        <span class="use use--toilet"><svg viewBox="0 0 12 12"><path d="M2 1h2v5h6l-1 3H6v2H3V8L2 6z"/></svg>Toilet</span>
        <span class="use use--wet"><svg viewBox="0 0 12 12"><path d="M1 11V6a5 5 0 0 1 10 0h-2a3 3 0 0 0-6 0v5z"/></svg>Wet Areas</span>
        <span class="use use--sanitary"><svg viewBox="0 0 12 12"><path d="M4 0h2v5l4 7H1l3-7z"/></svg>Sanitary</span>
        <span class="use use--bath"><svg viewBox="0 0 12 12"><path d="M1 2h8v2H3v2h6v2H3v3H1z"/></svg>Bathroom</span>
      </div>
      <div class="photo-tiles" role="img" aria-label="Photo of stacked grey floor tiles"></div>
    </div>
    <p class="footer-left">Ideal for<br><span class="hl">quick and powerful<br>cleaning.</span></p>
    <p class="net"><span class="net-label">NET WT.</span><span class="net-value">1L</span></p>
  </section>

</body>
</html>
```